Private Maths Tuition Flyer based in London

I am opening up a new Maths tuition centre in North West London. The flyer will be delivered to over 8,000 homes within the immediate vicinity. The design should be suitable to be printed on an A5 sheet and read in a portrait orientation.

The flyer should include the following:

The headline statement should be "Private Maths Tuition"

Secondary headline statement is the following "GCSE, A-Levels, 11 Plus exams"

Some of service offerings/selling points are:

- Free first session
- Monthly Feedback reports
- Free support outside of sessions
- Clear Target grades
- Personalised Lesson plans
- Tangible Results

Another statement that should be featured is "Book your free session by visiting www.lernova.co.uk" or something similar to that.

"Contact Details:
020 7418 2903
enquiries@lernova.co.uk"

"Address:
Corbel Business and Innovation Centre
Wyvern Court
Larkfield Road
HA9 4QW"

Attached you'll see a logo which should be included and also a map of where we are. I am open to new images for the map if you guys have any, rather than a screen shot from plotway atlas but it should be clear to see.

I would like the content above to be displayed in a clear and concise manner that is easy to read. You have creative license on where this information should be displayed and where the images should be but on the whole it should look aesthetically pleasing on the eye.

Target Market(s)

Students, Parents. Parents who want maths tutors.

Industry/Entity Type

Tutoring

Font styles to use
Sans Serif

Requirements
Must have
• *logo*
• Private Maths Tuition
• GCSE, A-Levels, 11 Plus exams
• - Free first session
• - Monthly Feedback reports
• - Free support outside of sessions
• - Clear Target grades
• - Personalised Lesson plans
• - Tangible Results
• Book your free session by visiting www.lernova.co.uk" or something similar to that.
• Contact Details:
• 020 7418 2903
• enquiries@lernova.co.uk
• Address (*with map*):
• Corbel Business and Innovation Centre
• Wyvern Court
• Larkfield Road
• HA9 4QW
Nice to have
• similar colour scheme as the logo. creative background design.

```html
<!DOCTYPE html>
<html lang="en">
<head>
<meta charset="utf-8">
<title>Lernova – Private Maths Tuition Flyer</title>
<link href="https://fonts.googleapis.com/css2?family=Arimo:wght@400;700&display=swap" rel="stylesheet">
<style>
  :root {
    --brand-blue: #3f66b0;
    --deep-blue: #1f4fa8;
    --brand-orange: #ee6b1f;
    --brand-green: #8cc63f;
    --ink: #1c1c1c;
    --paper: #ffffff;
    --stage: #ecebe8;
  }
  * { box-sizing: border-box; margin: 0; padding: 0; }
  html, body {
    width: 1200px; height: 927px; overflow: hidden;
    background: var(--stage);
    font-family: "Arimo", Arial, sans-serif;
  }
  .flyer {
    position: absolute; left: 296px; top: 33px;
    width: 608px; height: 860px;
    background: var(--paper);
    overflow: hidden;
    box-shadow: 0 6px 22px rgba(0,0,0,.18);
  }
  .flyer-backdrop { position: absolute; inset: 0; }
  .brand {
    position: absolute; left: 46px; top: 44px;
    display: flex; align-items: center; gap: 10px;
  }
  .brand-dot { width: 16px; height: 16px; border-radius: 50%; background: var(--brand-green); }
  .brand-name { font-size: 34px; font-weight: 700; color: var(--brand-orange); letter-spacing: .5px; }
  .headline-banner {
    position: absolute; left: 30px; top: 112px;
    background: var(--brand-orange); color: #fff;
    font-size: 22px; font-weight: 700; letter-spacing: .5px;
    padding: 9px 18px 9px 20px;
    border-radius: 0 6px 6px 0;
  }
  .qualifications {
    position: absolute; left: 64px; top: 196px;
    color: #fff; font-size: 29px; font-weight: 400; line-height: 1.05;
  }
  .selling-points {
    position: absolute; left: 64px; top: 282px;
    list-style: none; color: #fff; font-size: 16px; line-height: 31px;
  }
  .selling-points li { position: relative; padding-left: 26px; }
  .selling-points li::before {
    content: "✱"; position: absolute; left: 0; top: 0;
    color: var(--brand-orange); font-size: 16px;
  }
  .booking {
    position: absolute; left: 30px; top: 604px;
  }
  .booking-lead { color: var(--deep-blue); font-size: 30px; font-weight: 700; }
  .booking-url { color: var(--brand-orange); font-size: 23px; font-weight: 700; margin-top: 2px; }
  .location-map {
    position: absolute; left: 30px; top: 690px;
    width: 350px; height: 140px;
    background: linear-gradient(135deg, #e6e3dc 0%, #dcd9d1 55%, #c7dcb0 100%);
  }
  .contact {
    position: absolute; left: 402px; top: 604px;
    color: var(--ink); font-size: 13.5px; line-height: 17px;
  }
  .contact-title {
    color: var(--deep-blue); font-size: 19px; font-weight: 700;
    padding-bottom: 4px; margin-bottom: 8px;
    border-bottom: 2px solid var(--brand-green); display: inline-block;
  }
  .contact-lines { margin-top: 52px; }
</style>
</head>
<body>
  <article class="flyer">
    <svg class="flyer-backdrop" width="608" height="860" viewBox="0 0 608 860" aria-hidden="true">
      <path d="M0,176 L300,176 L300,40 L608,40 L608,440 C470,470 300,520 0,610 Z" fill="var(--brand-blue)"/>
      <path d="M0,610 C300,520 470,470 608,440 L608,468 C460,490 300,545 0,640 Z" fill="var(--brand-green)"/>
      <path d="M0,620 C300,540 470,482 608,452 L608,470 C460,498 300,555 0,650 Z" fill="var(--paper)"/>
    </svg>
    <svg class="student-photo" style="position:absolute;left:300px;top:40px" width="308" height="430" viewBox="0 0 308 430" role="img" aria-label="Photo of a smiling student holding a folder">
      <defs>
        <linearGradient id="photoTone" x1="0" y1="0" x2="0" y2="1">
          <stop offset="0" stop-color="#5a4a44"/>
          <stop offset=".45" stop-color="#c9a08a"/>
          <stop offset="1" stop-color="#ece9e6"/>
        </linearGradient>
      </defs>
      <path d="M20,0 L308,0 L308,400 C210,418 120,410 20,395 Z" fill="url(#photoTone)"/>
    </svg>

    <div class="brand">
      <span class="brand-dot"></span>
      <span class="brand-name">Lernova</span>
    </div>

    <h1 class="headline-banner">PRIVATE MATHS TUITION</h1>

    <h2 class="qualifications">GCSE, A-Levels,<br>11 Plus exams</h2>

    <ul class="selling-points">
      <li>Free first session</li>
      <li>Monthly Feedback reports</li>
      <li>Free support outside of sessions</li>
      <li>Clear Target grades</li>
      <li>Personalised Lesson plans</li>
      <li>Tangible Results</li>
    </ul>

    <div class="booking">
      <p class="booking-lead">Book your free session</p>
      <p class="booking-url">by visiting www.lernova.co.uk</p>
    </div>

    <div class="location-map" role="img" aria-label="Street map showing the location of Corbel Business and Innovation Centre"></div>

    <address class="contact" style="font-style:normal">
      <h3 class="contact-title">Contact us</h3>
      <p>Corbel Business and Innovation Centre<br>Wyvern Court<br>Larkfield Road<br>HA9 4QW</p>
      <p class="contact-lines">020 7418 2903<br>enquiries@lernova.co.uk</p>
    </address>
  </article>
</body>
</html>
```